Technology Podcast Cover Art Design

Title: The Wavebreakers
Subtitle: A podcast about the future of all of us

site:

https://wavebreakers-show.example (ignore the colors/theme of site, we can change this as needed to suit new cover)

here is the description to give idea what podcast is about:
The Wavebreakers is like a longform KOVA Lecture, a podcast about the future of all of us where look at the technologies, trends and societal norms shaping our collective future. Here the world’s disruptive top minds share their passion projects and how advances in genomics, robotics, space travel, IoT, artificial intelligence and other exponential tech is converging to create the future of tomorrow.

Two minds are better than one, and the purpose of this podcast is to create a worldwide “neural network” of connected human creators to tackle society’s big problems like climate change, aging, inequality, disease… you name it.

The #1 problem plaguing humanity is short term thinking. If in-depth, unscripted conversations with the scientists, startups and thought leaders daring to dream bigger is your cup of tea, you have come to the right place.

--

Target audience:
similar to Kova.example, innovative creatives, scientists, startups, politicians... mainly smart people interested in future

Avoid:
DO NOT have a picture of a microphone in the cover art

What needs to be written:
the only thing that HAS to be written is: The Wavebreakers

you can also add the subtitle (but you don't have to): A podcast about the future of all of us

you can also add host info (but you don't have to): with Leon Pratt

--

in terms of colors, we would prefer bright colors, probably blue or orange but if you make an awesome cover we can use that instead

```html
<!DOCTYPE html>
<html lang="en">
<head>
<meta charset="utf-8">
<title>The Wavebreakers — Podcast Cover</title>
<link rel="stylesheet" href="https://fonts.googleapis.com/css2?family=Bebas+Neue&display=swap">
<style>
  :root {
    --bg-grey: #808184;
    --ink-dark: #3a3a3c;
    --accent-orange: #f7941d;
  }
  html, body {
    margin: 0;
    padding: 0;
    width: 1198px;
    height: 1200px;
    overflow: hidden;
    background: var(--bg-grey);
  }
  .cover {
    position: relative;
    width: 1198px;
    height: 1200px;
    background: var(--bg-grey);
    font-family: "Bebas Neue", "Arial Narrow", sans-serif;
  }
  .cover-art {
    display: block;
    width: 1198px;
    height: 1200px;
  }
  .show-title {
    font-family: "Bebas Neue", "Arial Narrow", sans-serif;
    font-weight: 400;
    fill: var(--ink-dark);
  }
  .show-title__article {
    font-size: 34px;
    letter-spacing: 6px;
  }
  .show-title__name {
    font-size: 272px;
  }
</style>
</head>
<body>
<main class="cover">
  <svg class="cover-art" viewBox="0 0 1198 1200" xmlns="http://www.w3.org/2000/svg">
    <defs>
      <linearGradient id="stroke-fade-top" x1="0" y1="0" x2="1" y2="1">
        <stop offset="0" stop-color="#3a3a3c" stop-opacity="0.9"/>
        <stop offset="0.5" stop-color="#f7941d" stop-opacity="0.8"/>
        <stop offset="1" stop-color="#808184" stop-opacity="0"/>
      </linearGradient>
      <linearGradient id="stroke-fade-bottom" x1="1" y1="1" x2="0" y2="0">
        <stop offset="0" stop-color="#f7941d" stop-opacity="0.9"/>
        <stop offset="0.5" stop-color="#3a3a3c" stop-opacity="0.85"/>
        <stop offset="1" stop-color="#808184" stop-opacity="0"/>
      </linearGradient>
    </defs>

    <rect class="backdrop" width="1198" height="1200" fill="var(--bg-grey)"/>

    <polygon class="brush-streaks brush-streaks--top" role="img"
             aria-label="Diagonal brush streaks in dark grey and orange"
             points="30,0 700,0 880,260 600,200 300,130 140,60"
             fill="url(#stroke-fade-top)"/>

    <polygon class="brush-streaks brush-streaks--bottom" role="img"
             aria-label="Diagonal brush streaks in dark grey and orange"
             points="1198,860 1198,1200 1000,1200 660,1150 470,1020 700,900 920,860"
             fill="url(#stroke-fade-bottom)"/>

    <g class="show-title">
      <text class="show-title show-title__article" x="601" y="486" text-anchor="middle">THE</text>
      <text class="show-title show-title__name" x="68" y="706"
            textLength="1062" lengthAdjust="spacingAndGlyphs">WAVEBREAKERS</text>
    </g>
  </svg>
</main>
</body>
</html>
```